PTA Meeting Poster

We are looking to create a poster to invite parents of our school to our monthly PTA Meeting.

The copy should include:

PTA Meeting
This Wednesday
8:40am
in the Multi Purpose Room

All Welcome!

```html
<!DOCTYPE html>
<html lang="en">
<head>
<meta charset="utf-8">
<title>PTA Meeting Poster</title>
<link rel="stylesheet" href="https://fonts.googleapis.com/css2?family=Russo+One&family=Ubuntu:wght@700&display=swap">
<style>
  :root {
    --paper: #fdf6f5;
    --streak: #f7dcdb;
    --crimson: #a1343c;
    --brown: #4a2119;
    --ghost-1: #f1e4e2;
    --ghost-2: #e8d2cf;
    --ghost-3: #dcbdb8;
    --ghost-4: #c8a29c;
    --band: #e3777e;
    --band-light: #f2a6aa;
    --band-pale: #f8cfd0;
    --white: #ffffff;
    --outline: #b2434a;
    --echo: #ef9ba0;
    --pin: #3b9fd6;
  }
  html, body { margin: 0; padding: 0; overflow: hidden; }
  body { width: 849px; height: 1200px; background: var(--paper); }
  .poster { display: block; width: 849px; height: 1200px; }
  .headline { font-family: "Russo One", "Arial Black", sans-serif; }
  .details { font-family: "Ubuntu", "Trebuchet MS", sans-serif; font-weight: 700; }
  .title-pta { fill: var(--crimson); }
  .title-meeting, .day { fill: var(--brown); }
  .echo-1 { fill: var(--ghost-1); }
  .echo-2 { fill: var(--ghost-2); }
  .echo-3 { fill: var(--ghost-3); }
  .echo-4 { fill: var(--ghost-4); }
  .info { fill: var(--white); stroke: var(--outline); stroke-width: 5; paint-order: stroke; stroke-linejoin: round; }
  .info-echo { fill: var(--echo); }
</style>
</head>
<body>
<svg class="poster" viewBox="0 0 849 1200" xmlns="http://www.w3.org/2000/svg">
  <g class="background">
    <rect width="849" height="1200" fill="var(--paper)"/>
    <polygon points="0,120 849,-60 849,0 0,40" fill="var(--streak)" opacity="0.6"/>
    <polygon points="0,300 849,80 849,130 0,360" fill="var(--streak)" opacity="0.5"/>
    <polygon points="0,520 849,360 849,390 0,560" fill="var(--streak)" opacity="0.4"/>
  </g>

  <g class="info-band">
    <polygon points="0,730 849,600 849,1200 0,1200" fill="var(--band)"/>
    <polygon points="0,730 849,600 849,660 0,800" fill="var(--band-pale)"/>
    <polygon points="0,820 849,690 849,720 0,860" fill="var(--band-light)"/>
    <polygon points="0,960 849,850 849,880 0,1000" fill="var(--band-light)" opacity="0.7"/>
    <polygon points="0,1110 849,1010 849,1060 0,1170" fill="var(--band-light)" opacity="0.6"/>
  </g>

  <g class="pins">
    <rect role="img" aria-label="Blue push pin" x="60" y="30" width="40" height="70" rx="14" fill="var(--pin)" transform="rotate(-35 80 65)"/>
    <rect role="img" aria-label="Blue push pin" x="760" y="15" width="40" height="70" rx="14" fill="var(--pin)" transform="rotate(30 780 50)"/>
  </g>

  <g class="headline">
    <text class="title-pta" x="45" y="290" font-size="215" textLength="440" lengthAdjust="spacingAndGlyphs" transform="rotate(-10 45 290)">PTA</text>
    <text class="title-meeting" x="40" y="440" font-size="175" textLength="650" lengthAdjust="spacingAndGlyphs" transform="rotate(-10 40 440)">MEETING</text>

    <text class="echo-1" x="765" y="470" font-size="34" text-anchor="end" textLength="270" lengthAdjust="spacingAndGlyphs" transform="rotate(-3 765 470)">WEDNESDAY</text>
    <text class="echo-2" x="765" y="518" font-size="44" text-anchor="end" textLength="340" lengthAdjust="spacingAndGlyphs" transform="rotate(-3 765 518)">WEDNESDAY</text>
    <text class="echo-3" x="765" y="565" font-size="50" text-anchor="end" textLength="400" lengthAdjust="spacingAndGlyphs" transform="rotate(-3 765 565)">WEDNESDAY</text>
    <text class="echo-4" x="765" y="612" font-size="54" text-anchor="end" textLength="450" lengthAdjust="spacingAndGlyphs" transform="rotate(-3 765 612)">WEDNESDAY</text>
    <text class="day" x="778" y="690" font-size="80" text-anchor="end" textLength="470" lengthAdjust="spacingAndGlyphs" transform="rotate(-3 778 690)">WEDNESDAY</text>
  </g>

  <g class="details">
    <text class="info" x="200" y="845" font-size="150" textLength="495" lengthAdjust="spacingAndGlyphs" transform="rotate(-8 200 845)">8:40am</text>
    <text class="info" x="470" y="895" font-size="52" text-anchor="middle" transform="rotate(-8 470 895)">in the</text>
    <text class="info" x="200" y="985" font-size="70" textLength="590" lengthAdjust="spacingAndGlyphs" transform="rotate(-8 200 985)">Multi Purpose Room</text>
    <text class="info" x="170" y="1100" font-size="118" textLength="640" lengthAdjust="spacingAndGlyphs" transform="rotate(-8 170 1100)">All Welcome!</text>
    <text class="info-echo" x="170" y="1190" font-size="90" textLength="500" lengthAdjust="spacingAndGlyphs" transform="rotate(-8 170 1190)">All Welcome</text>
  </g>
</svg>
</body>
</html>
```